Wendell's UPDATE -Across the Board

Insurance Agent Business card and probably everything else !
Been in business for over 35 years and never took the time to update so really like the black-gold combo but open for suggestions (Honestly, I have NO idea how this works but sounds very cool ) Attached are two samples that I enjoy. The black and gold option is my favorite so looking for something like that!

```html
<!DOCTYPE html>
<html lang="en">
<head>
<meta charset="utf-8">
<title>Wendell S Marlow – Business Card</title>
<link rel="stylesheet" href="https://fonts.googleapis.com/css2?family=Comfortaa:wght@400;600;700&family=Montserrat:wght@400;500;600&display=swap">
<style>
  :root{
    --bg:#1c1c1c;
    --card-black:#0b0b0b;
    --gold:#e9bd2e;
    --gold-soft:#d8b54a;
    --gold-fill:#fcc71a;
    --gold-light:#ffdb63;
    --silver:#dcdbd4;
    --ink:#1a1a1a;
    --white:#f3f3f3;
  }
  *{box-sizing:border-box;margin:0;padding:0}
  html,body{width:1200px;height:1200px;overflow:hidden;background:var(--bg)}
  .canvas{
    position:relative;width:1200px;height:1200px;
    background:radial-gradient(circle at 50% 45%,#2a2a2a 0%,var(--bg) 70%);
    font-family:"Comfortaa",sans-serif;
  }
  .sheet-title{
    position:absolute;top:34px;left:0;width:100%;text-align:center;
    font-family:"Montserrat",sans-serif;font-weight:400;font-size:34px;
    color:var(--gold);letter-spacing:1px;
  }
  .card{
    position:absolute;left:180px;width:840px;height:480px;
    border-radius:30px;overflow:hidden;background:var(--card-black);
    box-shadow:0 0 18px rgba(255,255,255,.18),0 18px 40px rgba(0,0,0,.6);
  }
  .card--back{top:110px}
  .card--front{top:620px}

  /* Back */
  .back-brand{
    position:absolute;top:0;left:0;width:100%;height:100%;
    display:flex;flex-direction:column;align-items:center;justify-content:center;gap:34px;
  }
  .brand-mark{display:flex;align-items:center;gap:18px}
  .brand-mark__square{width:22px;height:22px;background:var(--gold-soft)}
  .brand-mark__name{font-weight:400;color:var(--gold-soft);font-size:52px;letter-spacing:1px}
  .back-url{
    font-family:"Montserrat",sans-serif;font-weight:600;font-size:18px;
    color:var(--gold);letter-spacing:9px;
  }

  /* Front */
  .front-art{position:absolute;inset:0;width:100%;height:100%}
  .front-brand{position:absolute;left:52px;top:96px;width:330px;text-align:center}
  .front-brand .brand-mark{justify-content:center;gap:12px}
  .front-brand .brand-mark__square{width:16px;height:16px}
  .front-brand .brand-mark__name{font-size:34px}
  .front-est{
    margin-top:22px;font-family:"Montserrat",sans-serif;font-weight:600;
    font-size:20px;letter-spacing:10px;color:var(--gold);
  }
  .identity{position:absolute;right:52px;top:64px;text-align:right}
  .identity__name{font-weight:700;font-size:40px;color:var(--gold);letter-spacing:2px}
  .identity__role{margin-top:8px;font-family:"Montserrat",sans-serif;font-size:17px;color:var(--white);letter-spacing:.5px}

  .contact-list{
    position:absolute;right:40px;top:276px;list-style:none;
    font-family:"Comfortaa",sans-serif;font-weight:600;color:var(--ink);
    text-align:right;
  }
  .contact-list li{display:flex;justify-content:flex-end;align-items:center;gap:12px;font-size:20px;height:36px}
  .contact-icon{
    width:28px;height:28px;border:2px solid var(--ink);border-radius:50%;
    display:flex;align-items:center;justify-content:center;flex:none;
  }
  .contact-icon svg{width:14px;height:14px}
  .contact-address{margin-top:8px;font-size:20px;line-height:28px;padding-right:40px}
</style>
</head>
<body>
<main class="canvas">
  <h1 class="sheet-title">Revised Business Card- Mockup 3</h1>

  <section class="card card--back" aria-label="Card back">
    <div class="back-brand">
      <div class="brand-mark">
        <span class="brand-mark__square"></span>
        <span class="brand-mark__name">Wendell S Marlow</span>
      </div>
      <p class="back-url">WWW.WSMCOVER.COM</p>
    </div>
  </section>

  <section class="card card--front" aria-label="Card front">
    <svg class="front-art" viewBox="0 0 840 480" preserveAspectRatio="none" aria-hidden="true">
      <defs>
        <linearGradient id="goldFill" x1="0" y1="1" x2="1" y2="0">
          <stop offset="0" stop-color="#ffe07a"/>
          <stop offset=".5" stop-color="#fdc80e"/>
          <stop offset="1" stop-color="#f7b21a"/>
        </linearGradient>
        <linearGradient id="silverBand" x1="0" y1="0" x2="1" y2="0">
          <stop offset="0" stop-color="#f2f1ea"/>
          <stop offset=".55" stop-color="#d2d0c6"/>
          <stop offset=".8" stop-color="#f4f3ee"/>
          <stop offset="1" stop-color="#a9a79f"/>
        </linearGradient>
      </defs>
      <path d="M0,318 C230,390 470,300 650,250 C740,226 800,236 840,255 L840,480 L0,480 Z" fill="url(#silverBand)"/>
      <path d="M0,346 C230,412 470,318 650,270 C740,248 800,258 840,278 L840,480 L0,480 Z" fill="#fcc71a"/>
      <path d="M0,356 C230,422 470,328 650,280 C740,258 800,268 840,288 L840,480 L0,480 Z" fill="#e8e7e0"/>
      <path d="M0,368 C230,434 470,340 650,292 C740,270 800,280 840,300 L840,480 L0,480 Z" fill="url(#goldFill)"/>
    </svg>

    <div class="front-brand">
      <div class="brand-mark">
        <span class="brand-mark__square"></span>
        <span class="brand-mark__name">Wendell S Marlow</span>
      </div>
      <p class="front-est">~ EST. 1985 ~</p>
    </div>

    <div class="identity">
      <p class="identity__name">Wendell S Marlow</p>
      <p class="identity__role">Insurance &amp; Financial Consultant</p>
    </div>

    <ul class="contact-list">
      <li>555-438-0173
        <span class="contact-icon"><svg viewBox="0 0 24 24"><path d="M6 2l4 4-2 3c1.5 3 4 5.5 7 7l3-2 4 4-3 4C10 21 3 14 2 5z" fill="#1a1a1a"/></svg></span>
      </li>
      <li>555-433-0166
        <span class="contact-icon"><svg viewBox="0 0 24 24"><rect x="6" y="2" width="12" height="20" rx="2" fill="#1a1a1a"/><rect x="8" y="5" width="8" height="11" fill="#fcc71a"/></svg></span>
      </li>
      <li>wendell@wsmcover.com
        <span class="contact-icon"><svg viewBox="0 0 24 24"><rect x="2" y="5" width="20" height="14" rx="2" fill="none" stroke="#1a1a1a" stroke-width="2.5"/><path d="M3 6l9 7 9-7" fill="none" stroke="#1a1a1a" stroke-width="2.5"/></svg></span>
      </li>
      <li>www.wsmcover.com
        <span class="contact-icon"><svg viewBox="0 0 24 24"><circle cx="12" cy="12" r="9" fill="none" stroke="#1a1a1a" stroke-width="2.5"/><ellipse cx="12" cy="12" rx="4" ry="9" fill="none" stroke="#1a1a1a" stroke-width="2"/><path d="M3 12h18" stroke="#1a1a1a" stroke-width="2"/></svg></span>
      </li>
      <li class="contact-address" style="display:block;height:auto">2140 Harbor Crest Avenue, Suite 310-4<br>Palm Hollow, FL 33099</li>
    </ul>
  </section>
</main>
</body>
</html>
```